I NEED A BUSINESS CARD. (TWO SIDE DESIGN) . PLEASE USE THE FOLLOWING INFORMATION AND LOGO. THANKS.
Name: Mavick Toleporan (Owner)
Bus Tel.: (416) 555-0187
Cell: 416 555 0142
Email: info@bluefernco.example
Web: bluefernco.example
Address: 238 Corlwick Avenue Unit 17. Toronto, ON X9Q 2Z7. Scarborough.

```html
<!DOCTYPE html>
<html lang="en">
<head>
<meta charset="utf-8">
<title>Blue Fern Homestore — Business Card</title>
<link rel="stylesheet" href="https://fonts.googleapis.com/css2?family=Lato:wght@400;700&display=swap">
<style>
  :root {
    --stage: #2b2b2d;
    --paper: #ffffff;
    --slate: #3a3b3e;
    --slate-deep: #2f3033;
    --brand-red: #e3233b;
    --ink-light: #f1f1f1;
    --ink-muted: #b9babd;
    --icon-grey: #8d8e92;
  }
  * { box-sizing: border-box; margin: 0; padding: 0; }
  html, body { width: 1200px; height: 900px; overflow: hidden; }
  body {
    background: var(--stage);
    font-family: "Lato", Arial, sans-serif;
    position: relative;
  }
  .card {
    position: absolute;
    border-radius: 22px;
    overflow: hidden;
    box-shadow: 0 18px 40px rgba(0,0,0,0.45);
  }

  /* Front */
  .card-front {
    left: 560px; top: 150px;
    width: 560px; height: 320px;
    background: var(--paper);
    display: flex; flex-direction: column; align-items: center; justify-content: center;
  }
  .brand {
    display: flex; align-items: center; gap: 14px;
  }
  .brand-dot {
    width: 22px; height: 22px; border-radius: 50%;
    background: var(--brand-red);
    flex: none;
  }
  .brand-name {
    font-weight: 700;
    color: var(--brand-red);
    text-transform: uppercase;
    letter-spacing: 2px;
    line-height: 1;
  }
  .card-front .brand-name { font-size: 34px; }
  .rule {
    width: 46px; height: 3px; background: var(--brand-red);
    margin: 26px 0 22px;
  }
  .front-address {
    display: flex; align-items: center; gap: 8px;
    color: var(--brand-red);
    font-size: 15px;
  }
  .front-address svg { width: 14px; height: 18px; flex: none; }

  /* Back */
  .card-back {
    left: 90px; top: 250px;
    width: 330px; height: 560px;
    background: var(--slate);
  }
  .back-top {
    height: 200px;
    background: var(--paper);
    display: flex; align-items: center; justify-content: center;
  }
  .card-back .brand-name { font-size: 22px; letter-spacing: 1.5px; }
  .card-back .brand-dot { width: 16px; height: 16px; }
  .back-body {
    position: relative;
    height: 360px;
    background: linear-gradient(160deg, var(--slate) 0%, var(--slate-deep) 100%);
    padding: 30px 28px 0 28px;
  }
  .contact-list { list-style: none; }
  .contact-row {
    display: flex; align-items: center; gap: 16px;
    color: var(--ink-light);
    font-size: 15px;
    margin-bottom: 16px;
  }
  .contact-row .icon {
    width: 28px; height: 28px; border-radius: 50%;
    background: var(--brand-red);
    display: flex; align-items: center; justify-content: center;
    flex: none;
  }
  .contact-row .icon.person { background: var(--icon-grey); }
  .contact-row .icon svg { width: 15px; height: 15px; }
  .person-name { font-size: 18px; line-height: 1.1; }
  .person-role { font-size: 12px; color: var(--ink-muted); }
  .back-address {
    margin: 12px 0 0 44px;
    color: var(--ink-light);
    font-size: 15px;
    line-height: 1.45;
  }
</style>
</head>
<body>

  <section class="card card-back" aria-label="Business card, contact side">
    <div class="back-top">
      <div class="brand">
        <span class="brand-dot"></span>
        <span class="brand-name">Blue Fern Homestore</span>
      </div>
    </div>
    <div class="back-body">
      <ul class="contact-list">
        <li class="contact-row">
          <span class="icon person">
            <svg viewBox="0 0 16 16"><circle cx="8" cy="5" r="3.2" fill="#fff"/><path d="M2 15c0-3.5 2.7-5.5 6-5.5s6 2 6 5.5z" fill="#fff"/></svg>
          </span>
          <div>
            <div class="person-name">Mavick Toleporan</div>
            <div class="person-role">Owner</div>
          </div>
        </li>
        <li class="contact-row">
          <span class="icon">
            <svg viewBox="0 0 16 16"><rect x="4" y="1" width="8" height="14" rx="1.5" fill="none" stroke="#fff" stroke-width="1.6"/><circle cx="8" cy="12.3" r="0.9" fill="#fff"/></svg>
          </span>
          <span>(416) 555-0187</span>
        </li>
        <li class="contact-row">
          <span class="icon">
            <svg viewBox="0 0 16 16"><path d="M3.5 1.5l2.5 3-1.5 1.6c.8 1.9 2.3 3.4 4.2 4.2l1.6-1.5 3 2.5-1.6 2.3C6.5 13.4 2.6 9.5 1.2 3.1z" fill="#fff"/></svg>
          </span>
          <span>416 555 0142</span>
        </li>
        <li class="contact-row">
          <span class="icon">
            <svg viewBox="0 0 16 16"><rect x="1.5" y="3.5" width="13" height="9" rx="1" fill="none" stroke="#fff" stroke-width="1.5"/><path d="M1.8 4l6.2 4.8L14.2 4" fill="none" stroke="#fff" stroke-width="1.5"/></svg>
          </span>
          <span>info@bluefernco.example</span>
        </li>
        <li class="contact-row">
          <span class="icon">
            <svg viewBox="0 0 16 16"><circle cx="8" cy="8" r="6.3" fill="none" stroke="#fff" stroke-width="1.4"/><ellipse cx="8" cy="8" rx="2.8" ry="6.3" fill="none" stroke="#fff" stroke-width="1.2"/><path d="M1.8 8h12.4" stroke="#fff" stroke-width="1.2"/></svg>
          </span>
          <span>bluefernco.example</span>
        </li>
      </ul>
      <p class="back-address">238 Corlwick Avenue Unit 17. Toronto,<br>ON X9Q 2Z7. Scarborough.</p>
    </div>
  </section>

  <section class="card card-front" aria-label="Business card, brand side">
    <div class="brand">
      <span class="brand-dot"></span>
      <span class="brand-name">Blue Fern Homestore</span>
    </div>
    <span class="rule"></span>
    <p class="front-address">
      <svg viewBox="0 0 14 18"><path d="M7 0C3.1 0 0 3 0 6.8 0 11.5 7 18 7 18s7-6.5 7-11.2C14 3 10.9 0 7 0z" fill="currentColor"/><circle cx="7" cy="6.8" r="2.5" fill="#fff"/></svg>
      238 Corlwick Avenue Unit 17. Toronto, ON X9Q 2Z7. Scarborough
    </p>
  </section>

</body>
</html>
```